Paranormal Romance Author needs unique, eye-catching book covers for an entire series of books!

Author Mara Quillon is in need of outstanding, mind-blowing, unique, and eye-catching book covers for a paranormal romance series, called Wandering Embers. Initially we will only be asking for a design for the first book stated at the current price. Book 1: Wandering Embers. Once a winner is picked, the rest of the series will be negotiated (up to five more books. Possibly more.) The titles will be as following. Wandering Embers, Silver Embers, Hollow Embers, etc. Check out the unofficial description below. And if you would like a better feel for the book, the first five chapters have been attached as a document for your reading pleasure. :)In the hot and unforgiving Arizona desert, seventeen-year old Tessa Lindqvist finds herself in the most impossible of situations. When her boyfriend of ten years breaks up with her, she takes off into a storm, crashes her car, and dies. But then again, does she really? She is awaken during a battle and has been bitten. By a vampire. That's when young Captain Cole Harwick finds her. Going against everything he's been taught and trained for, he saves her from being killed by his men. She is still human after all. And a beautiful young girl at that. How could he bring himself to kill her?Tessa and Cole's tale is one of trials and torture, love and loss, but most of all, accepting one's own death. Will Cole safely see Tessa through her transformation to being a vampire? Will Tessa accept the immortal life that has ben thrust upon her? And will the two be able to part when the time comes, going off in their rightful positions, as enemies?Along with the author's name: Mara Quillon, and the book title, a tag-line shall be on the cover as well.Book 1: Wandering Embers, will have the tag-line "Do you know what dying feels like?"Images have been attached of book covers or art that speak to the author in her same genre. If human models are used on the cover, the author would prefer them to be smaller and farther away. But models are not imperative. If people are used, no bare-chested men that normally adorn adult romance covers. This series is guided for a young adult audience and must be done tastefully and fantastically, keeping a gothic, romantic feel. Basically the author seeks award-winning best-selling covers that are different and eye-catching, keeping the series covers similar for branding purposes. Think "series" and create a cover that can have a running theme. Have fun with this and most importantly, think outside of the box!!!*Note about character description. If model is used for Tessa, she is a young female aged 17 and has long white-blonde hair. Her eyes are violet-purple. The author prefers not to have a model for the male character at this point. And doesn't particularly care if a model is used as long as the design is striking.
Updates

4 participation payments have been added at $20.00 each. Thank you designers for all of your hard work. I know all too well how much goes into every design. :D Added Thursday, February 19, 2015

Just so everyone knows where they stand I have rated most of the designs. If you have a four or five star you are in the running for the win and may be asked to make some minor changes. If you have three or less stars, please feel free to resubmit a different design. If I have not yet rated your design it is because I am undecided at this time. A few days before the contest end date I will be running a pole to get feedback from colleagues, which may help me to make a better decision. At that point I will let the designers know where they stand and if they wish to resubmit a last design or two they can do so at that time. But please, for ANY of you that wish to keep submitting, feel free. I love seeing different ideas. I am also considering adding a second place prize, because I know how much work goes into this process. I appreciate everyone's submissions and thank you greatly for your time. -Mara Added Monday, February 23, 2015

Target Market(s)

Young adult and adult readers. Female mostly, some male, ages 15-38. :D

Industry/Entity Type

Adult

Font styles to use
Serif
Decorative
Script

Requirements
Must have
• The tagline 'Do you know what dying feels like?' must be somewhere on the book.
• Other than that, there are no must-haves but some ideas are...*Think magical, mystical, dreamy, romantic. *A close-up of a tombstone with the title engraved on it? Fog? Smoke? Maybe a flower at the bottom? Ivy? Vines?*Or anything with withering branches, moons, birds.*This story is set in the desert, so maybe desert scenery? But beautifully morbid?*If a model is used, one in distress, arms wrapped around knees? Suffering? If model is used, must have enough different shots of her to fill out an entire book series of six or possibly more.* I actually designed the lark tamsworth covers for myself. (attached) I love the whole broken up pictures idea. But I just can't seem to get it right. LOL. :D

```html
<!DOCTYPE html>
<html lang="en">
<head>
<meta charset="utf-8">
<title>Wandering Embers — Cover Spread</title>
<link rel="stylesheet" href="https://fonts.googleapis.com/css2?family=Federo&family=Libre+Baskerville:ital@1&family=Tinos:wght@400;700&display=swap">
<style>
  :root {
    --paper: #ffffff;
    --blush: #f6dede;
    --blush-light: #fdf4f3;
    --blush-deep: #e9c2c2;
    --ink: #111111;
    --spine: #0b0b0b;
    --blood: #c0141a;
    --ember: #d9262c;
    --hair: #d8a45e;
    --skin: #f1d3c6;
    --white: #ffffff;
  }
  * { margin: 0; padding: 0; box-sizing: border-box; }
  html, body {
    width: 1200px;
    height: 1000px;
    overflow: hidden;
    background: var(--paper);
  }
  .spread {
    position: relative;
    width: 1200px;
    height: 1000px;
  }
  .jacket {
    position: absolute;
    left: 0;
    top: 75px;
    width: 1200px;
    height: 850px;
  }
  .panel-texture {
    position: absolute;
    top: 0;
    height: 850px;
    background:
      linear-gradient(90deg, rgba(17,17,17,0.55) 0, rgba(17,17,17,0) 34px),
      linear-gradient(270deg, rgba(17,17,17,0.55) 0, rgba(17,17,17,0) 34px),
      radial-gradient(ellipse at 50% 45%, var(--blush-light) 0%, var(--blush) 55%, var(--blush-deep) 88%, #b98f8f 100%);
    border-left: 12px solid var(--ink);
    border-right: 12px solid var(--ink);
  }
  .back-texture { left: 0; width: 548px; }
  .front-texture { left: 655px; width: 545px; }
  .front-texture {
    background:
      radial-gradient(ellipse at 25% 72%, rgba(192,20,26,0.18) 0%, rgba(192,20,26,0) 30%),
      radial-gradient(ellipse at 80% 82%, rgba(192,20,26,0.14) 0%, rgba(192,20,26,0) 28%),
      linear-gradient(90deg, rgba(17,17,17,0.55) 0, rgba(17,17,17,0) 34px),
      linear-gradient(270deg, rgba(17,17,17,0.55) 0, rgba(17,17,17,0) 34px),
      radial-gradient(ellipse at 50% 45%, var(--blush-light) 0%, var(--blush) 55%, var(--blush-deep) 88%, #b98f8f 100%);
  }

  .back-cover {
    position: absolute;
    left: 70px;
    top: 80px;
    width: 405px;
    font-family: "Tinos", serif;
    font-weight: 700;
    font-size: 15px;
    line-height: 29.6px;
    text-align: center;
    color: var(--ink);
  }

  .spine {
    position: absolute;
    left: 548px;
    top: 0;
    width: 107px;
    height: 850px;
    background: var(--spine);
  }
  .spine-title,
  .spine-author {
    position: absolute;
    left: 54px;
    white-space: nowrap;
    transform-origin: 0 0;
    transform: rotate(90deg) translateY(-50%);
  }
  .spine-title {
    top: 90px;
    font-family: "Federo", sans-serif;
    font-size: 46px;
    color: var(--white);
    text-shadow: 0 0 8px var(--ember), 0 0 14px var(--blood);
  }
  .spine-author {
    top: 575px;
    font-family: "Tinos", serif;
    font-size: 34px;
    color: var(--blood);
  }

  .front-cover {
    position: absolute;
    left: 655px;
    top: 0;
    width: 545px;
    height: 850px;
  }
  .tagline {
    position: absolute;
    top: 66px;
    left: 0;
    width: 100%;
    text-align: center;
    font-family: "Libre Baskerville", serif;
    font-style: italic;
    font-size: 24px;
    color: var(--blood);
  }
  .figure {
    position: absolute;
    left: 140px;
    top: 170px;
    width: 250px;
    height: 510px;
    border-radius: 50% 50% 38% 38% / 30% 30% 22% 22%;
    background:
      linear-gradient(180deg,
        var(--hair) 0%, #c98d48 26%, #e6c29a 40%, var(--skin) 50%,
        #e07a6e 64%, var(--ember) 80%, #a4161b 100%);
    box-shadow: 0 0 40px 12px rgba(217, 38, 44, 0.45);
  }
  .title {
    position: absolute;
    top: 362px;
    left: 0;
    width: 100%;
    text-align: center;
    font-family: "Federo", sans-serif;
    font-weight: 400;
    font-size: 98px;
    line-height: 122px;
    color: var(--ink);
    letter-spacing: -3px;
    text-shadow: 0 0 10px rgba(255,255,255,0.35);
  }
  .title span { display: block; }
  .author {
    position: absolute;
    top: 742px;
    left: 0;
    width: 100%;
    text-align: center;
    font-family: "Tinos", serif;
    font-size: 44px;
    letter-spacing: -1px;
    color: var(--ink);
  }
</style>
</head>
<body>
<main class="spread">
  <section class="jacket">
    <div class="panel-texture back-texture" role="img" aria-label="Pale blush background covered in black cracked-earth vein texture"></div>
    <div class="panel-texture front-texture" role="img" aria-label="Pale blush background covered in black and red cracked-earth vein texture"></div>

    <article class="back-cover">
      <p>In the hot and unforgiving Arizona desert, seventeen-year old Tessa Lindqvist finds herself in the most impossible of situations. When her boyfriend of ten years breaks up with her, she takes off into a storm, crashes her car, and dies. But then again, does she really? She is awaken during a battle and has been bitten. By a vampire. That's when young Captain Cole Harwick finds her. Going against everything he's been taught and trained for, he saves her from being killed by his men. She is still human after all. And a beautiful young girl at that. How could he bring himself to kill her?</p>
      <p>Tessa and Cole's tale is one of trials and torture, love and loss, but most of all, accepting one's own death. Will Cole safely see Tessa through her transformation to being a vampire?</p>
      <p>Will Tessa accept the immortal life that has ben thrust upon her?</p>
      <p>And will the two be able to part when the time comes, going off in their rightful positions, as enemies?</p>
    </article>

    <aside class="spine">
      <h2 class="spine-title">Wandering Embers</h2>
      <p class="spine-author">Mara Quillon</p>
    </aside>

    <section class="front-cover">
      <p class="tagline">Do you know what dying feels like?</p>
      <div class="figure" role="img" aria-label="Photograph of a blonde girl curled up hugging her knees, head bowed, glowing in red light"></div>
      <h1 class="title"><span>Wandering</span><span>Embers</span></h1>
      <p class="author">Mara Quillon</p>
    </section>
  </section>
</main>
</body>
</html>
```